Bright Acorn day Nursery flyer

I need a great flyer to attract new parents. Bright Acorn Is a fantastic, warm and homely nursery in Westmere road SE6 London. We offer many things that other nurseries don't offer such as Spanish, Yoga, Music, Cooking classes and Handsign. We also have an amazing system called KINDTRAK that allows parents to get alerts on the KINDTRAK app about their children daily activities and even developmental reports. Parents are able to share with the nursery great moments and put pictures and videos through the app. We also offer the parent camera, an extremely safe system that allows parents to log in and see their children whilst they are engaged in exciting activities.
Full details of Nursery
87 Westmere road
SE6 4QP
02084417260
www.brightacornhollis.co.uk
Social Page
brightacorndaynursery@brightacornhollis.co.uk
Updates

double sided or mini brochure type

Hi Please keep it simple and clean I feel the designs are a good attempt thank you but they are very busy and I just want to add important points a lot of the designs have too many colours, too much text etc Thank you!

https://www.facebook.com/brightacornhollis.co.uk/

Target Market(s)

parents of children 0-5

Industry/Entity Type

Childcare

Colors

Designer to choose colors to be used in the design.

Requirements
Must have
• colour and pictures but clean design

```html
<!DOCTYPE html>
<html lang="en">
<head>
<meta charset="utf-8">
<title>Bright Acorn Day Nursery – Flyer</title>
<link rel="stylesheet" href="https://fonts.googleapis.com/css2?family=Fredoka:wght@500;600&family=Open+Sans:wght@400;600;700&family=Roboto:wght@400;500;700&display=swap">
<style>
  :root {
    --teal: #17a697;
    --navy-blue: #3a55a6;
    --green: #1d9a4c;
    --pink: #e5267f;
    --purple: #8a2a92;
    --purple-dark: #6b1f73;
    --sky: #5bbcd7;
    --beige: #efe8dc;
    --ink: #2a2a2a;
    --white: #ffffff;
  }
  * { box-sizing: border-box; margin: 0; padding: 0; }
  html, body { width: 1041px; height: 1200px; overflow: hidden; background: var(--white); }
  .flyer { position: relative; width: 1041px; height: 1200px; overflow: hidden; font-family: "Open Sans", sans-serif; color: var(--ink); }

  .hero { position: absolute; left: 0; top: 0; width: 1041px; height: 560px; }

  .brand { position: absolute; left: 39px; top: 148px; width: 300px; text-align: center;
    font-family: "Fredoka", sans-serif; font-weight: 600; color: var(--teal); line-height: 1.1; }
  .brand-name { display: block; font-size: 40px; }
  .brand-sub { display: block; font-size: 17px; letter-spacing: 5px; }

  .now-open { position: absolute; left: 660px; top: 405px; width: 360px; height: 210px; }
  .now-open-text { position: absolute; left: 710px; top: 430px; width: 280px; text-align: center;
    font-family: "Fredoka", sans-serif; font-weight: 600; font-size: 58px; line-height: 1; color: var(--white); }

  .welcome { position: absolute; left: 47px; top: 530px; font-family: "Fredoka", sans-serif; font-weight: 600; }
  .welcome-line1 { display: block; font-size: 40px; color: var(--teal); line-height: 44px; }
  .welcome-line2 { display: block; font-size: 60px; color: var(--navy-blue); line-height: 62px; }
  .welcome-rule { position: absolute; left: 50px; top: 646px; width: 290px; height: 5px; background: var(--green); }

  .intro { position: absolute; left: 50px; top: 674px; width: 948px; font-size: 13.5px; font-weight: 600; line-height: 1.5; }

  .offer-tab { position: absolute; left: 0; top: 773px; width: 322px; height: 46px; background: var(--sky);
    border-radius: 0 23px 23px 0; color: var(--white); font-family: "Fredoka", sans-serif; font-weight: 600;
    font-size: 34px; line-height: 46px; padding-left: 48px; }
  .offer-list { position: absolute; left: 47px; top: 834px; list-style: none; font-family: "Fredoka", sans-serif; font-weight: 600; font-size: 35px; line-height: 40px; }
  .offer-list li { display: flex; align-items: center; gap: 12px; }
  .offer-list svg { width: 26px; height: 26px; flex: none; }
  .c-green { color: var(--green); } .c-ink { color: var(--ink); } .c-blue { color: var(--navy-blue); }
  .c-pink { color: var(--pink); } .c-teal { color: var(--teal); }

  .app-box { position: absolute; left: 522px; top: 815px; width: 519px; height: 260px; background: var(--beige); border-radius: 90px 0 0 0; }
  .app-copy { position: absolute; left: 588px; top: 852px; font-family: "Roboto", sans-serif; line-height: 1; }
  .app-copy .lead { display: block; font-size: 38px; color: var(--ink); }
  .app-copy .lead-small { display: block; font-size: 30px; color: var(--ink); margin-top: 2px; }
  .app-copy .accent { display: block; font-size: 32px; font-weight: 700; color: var(--pink); margin-top: 4px; }
  .app-brand { position: absolute; left: 896px; top: 950px; width: 130px; text-align: center; font-family: "Roboto", sans-serif;
    font-weight: 700; color: var(--ink); font-size: 22px; line-height: 1.3; }

  .contact-band { position: absolute; left: 0; top: 0; width: 1041px; height: 1200px; }
  .contact { position: absolute; left: 560px; top: 1040px; width: 470px; text-align: center; color: var(--white); }
  .contact-phone-icon { width: 30px; height: 30px; display: block; margin: 0 auto 4px; }
  .contact-phone { font-family: "Open Sans", sans-serif; font-weight: 700; font-size: 34px; line-height: 1.1; letter-spacing: .5px; }
  .contact-web { display: block; margin: 6px auto 0; width: 440px; height: 30px; border: 2px solid var(--white); border-radius: 15px;
    background: rgba(255,255,255,.12); font-size: 19px; line-height: 26px; }
  .contact-web b { font-weight: 700; }
  .contact-small { font-size: 15px; line-height: 1.35; margin-top: 4px; }

  .address { position: absolute; left: 40px; top: 1100px; font-weight: 700; font-size: 32px; line-height: 45px; color: var(--ink); font-style: normal; }
  .address-line { display: flex; align-items: center; gap: 8px; }
  .address-line svg { width: 30px; height: 32px; }
  .address-indent { padding-left: 38px; }
</style>
</head>
<body>
<main class="flyer">

  <svg class="hero" viewBox="0 0 1041 560">
    <defs>
      <linearGradient id="photoTone" x1="0" y1="0" x2="1" y2="1">
        <stop offset="0" stop-color="#f3eee6"/>
        <stop offset="0.45" stop-color="#f6d9c9"/>
        <stop offset="0.7" stop-color="#e9c33c"/>
        <stop offset="1" stop-color="#d93a3a"/>
      </linearGradient>
    </defs>
    <path role="img" aria-label="Photo of happy children sitting on a colourful play parachute with arms raised"
      d="M0 0 H1041 V340 C960 420 880 470 770 490 C640 515 520 500 360 440 C230 390 110 360 0 365 Z" fill="url(#photoTone)"/>
    <path d="M0 365 C110 360 230 390 360 440 C520 500 640 515 770 490 C880 470 960 420 1041 340 V372 C960 450 880 500 770 520 C620 548 500 525 350 470 C220 420 110 395 0 402 Z" fill="var(--navy-blue)"/>
    <path d="M0 470 C200 420 420 470 620 500" fill="none" stroke="#9fd8cf" stroke-width="1.5"/>
    <path d="M0 480 C220 440 430 480 640 505" fill="none" stroke="#e7a3c4" stroke-width="1.2"/>
  </svg>

  <div class="brand">
    <span class="brand-name">Bright Acorn</span>
    <span class="brand-sub">DAY NURSERY</span>
  </div>

  <svg class="now-open" viewBox="0 0 360 210" aria-hidden="true">
    <polygon points="200,150 290,150 210,205" fill="var(--purple-dark)"/>
    <polygon points="10,18 340,0 355,175 30,150" fill="var(--purple)"/>
  </svg>
  <div class="now-open-text">NOW<br>OPEN</div>

  <h1 class="welcome">
    <span class="welcome-line1">Welcome to Bright</span>
    <span class="welcome-line2">Acorn Day Nursery</span>
  </h1>
  <div class="welcome-rule"></div>

  <p class="intro">We are a privately owned, vibrant nursery offering your child a caring, family environment within the popular Hollis Estate. We offer high quality day care for all children from 3 months to 5 years, treating each child as a treasured individual. At Bright Acorn we know that choosing the best nursery for your child is vital but it can seem very daunting. You need to be absolutely sure you have made the right decision to give you peace of mind.</p>

  <div class="offer-tab">WE OFFER</div>
  <ul class="offer-list">
    <li class="c-green"><svg viewBox="0 0 24 24"><path d="M3 13l6 6L21 5" fill="none" stroke="var(--green)" stroke-width="2.5"/></svg>Spanish,</li>
    <li class="c-ink"><svg viewBox="0 0 24 24"><path d="M3 13l6 6L21 5" fill="none" stroke="var(--green)" stroke-width="2.5"/></svg>Yoga</li>
    <li class="c-blue"><svg viewBox="0 0 24 24"><path d="M3 13l6 6L21 5" fill="none" stroke="var(--green)" stroke-width="2.5"/></svg>Music</li>
    <li class="c-pink"><svg viewBox="0 0 24 24"><path d="M3 13l6 6L21 5" fill="none" stroke="var(--green)" stroke-width="2.5"/></svg>Cooking Classes</li>
    <li class="c-teal"><svg viewBox="0 0 24 24"><path d="M3 13l6 6L21 5" fill="none" stroke="var(--green)" stroke-width="2.5"/></svg>Handsign.</li>
  </ul>

  <div class="app-box"></div>
  <div class="app-copy">
    <span class="lead">DAILY</span>
    <span class="lead-small">NOTIFICATIONS</span>
    <span class="accent">FOR PARENTS</span>
    <span class="accent">THROUGH</span>
  </div>
  <div class="app-brand">KINDTRAK<br>APP</div>

  <svg class="contact-band" viewBox="0 0 1041 1200" aria-hidden="true">
    <path d="M0 1150 C200 1120 420 1150 560 1185" fill="none" stroke="#9fd8cf" stroke-width="1.5"/>
    <path d="M0 1165 C220 1135 430 1160 580 1195" fill="none" stroke="#e7a3c4" stroke-width="1.2"/>
    <path d="M360 1200 C470 1180 560 1150 590 1100 C620 1050 700 1022 820 1022 C920 1022 990 1050 1041 1085 V1200 Z" fill="var(--navy-blue)"/>
  </svg>

  <div class="contact">
    <svg class="contact-phone-icon" viewBox="0 0 24 24"><path d="M6.6 3.5l2.6 3-1.7 2.2c1.2 2.5 3.2 4.5 5.8 5.8l2.2-1.7 3 2.6-1.6 3.1C11 18.3 5.7 13 5.5 5.1z" fill="none" stroke="var(--white)" stroke-width="1.6" stroke-linejoin="round"/></svg>
    <div class="contact-phone">02084417260</div>
    <div class="contact-web">www.<b>brightacornhollis</b>.co.uk</div>
    <div class="contact-small">Social Page<br>brightacorndaynursery@brightacornhollis.co.uk</div>
  </div>

  <address class="address">
    <div class="address-line"><svg viewBox="0 0 24 26"><path d="M12 24s-7-7.5-7-13a7 7 0 0114 0c0 5.5-7 13-7 13z" fill="none" stroke="#555" stroke-width="1.6"/><circle cx="12" cy="11" r="2.6" fill="none" stroke="#555" stroke-width="1.6"/></svg>87 Westmere road</div>
    <div class="address-indent">SE6 4QP</div>
  </address>

</main>
</body>
</html>
```